Vornel Technologies business card design

We need a business card designed with our new logo. it would be great if the card could communicate it is a technology based company.

Target Market(s)

system integrators

Industry/Entity Type

technology, IOT

Contact Information for Business Card

Name, designation, Address, telephone number, email address

Requirements
Must have
• logo and company name
Nice to have
• something to do with technology

```html
<!DOCTYPE html>
<html lang="en">
<head>
<meta charset="utf-8">
<title>Vornel Technologies – Business Card</title>
<link rel="stylesheet" href="https://fonts.googleapis.com/css2?family=Roboto:wght@400;500&family=Rubik:wght@500&display=swap">
<style>
  :root {
    --stage: #e4e0d9;
    --charcoal: #3d3d3f;
    --orange: #f7941d;
    --paper: #ffffff;
    --ink: #3a3a3c;
  }
  * { margin: 0; padding: 0; box-sizing: border-box; }
  html, body {
    width: 900px;
    height: 1200px;
    overflow: hidden;
    background: var(--stage);
    font-family: "Roboto", sans-serif;
  }
  .canvas {
    position: relative;
    width: 900px;
    height: 1200px;
  }
  .card {
    position: absolute;
    left: 86px;
    width: 735px;
    height: 432px;
    border-radius: 22px;
    overflow: hidden;
    box-shadow: 0 6px 18px rgba(0,0,0,0.18);
  }
  .card--front {
    top: 136px;
    background: var(--charcoal);
    display: flex;
    align-items: center;
    justify-content: center;
  }
  .card--back {
    top: 633px;
    background: var(--paper);
  }
  .brand {
    display: flex;
    align-items: center;
    gap: 14px;
    font-family: "Roboto", sans-serif;
    font-weight: 500;
    letter-spacing: 0.5px;
  }
  .brand__square {
    width: 22px;
    height: 22px;
    background: var(--orange);
  }
  .brand--front .brand__name {
    color: var(--paper);
    font-size: 46px;
  }
  .brand--back {
    position: absolute;
    left: 37px;
    top: 78px;
  }
  .brand--back .brand__square { width: 18px; height: 18px; }
  .brand--back .brand__name {
    color: var(--charcoal);
    font-size: 36px;
  }
  .person {
    position: absolute;
    left: 145px;
    top: 222px;
  }
  .person__name {
    font-family: "Rubik", sans-serif;
    font-weight: 500;
    font-size: 27px;
    color: var(--orange);
    line-height: 32px;
  }
  .person__role {
    font-size: 18px;
    color: var(--ink);
    line-height: 26px;
  }
  .contact {
    position: absolute;
    left: 145px;
    top: 318px;
    list-style: none;
  }
  .contact__item {
    display: flex;
    align-items: center;
    gap: 10px;
    font-size: 18px;
    color: var(--ink);
    height: 26px;
    letter-spacing: 0.3px;
  }
  .contact__icon {
    width: 13px;
    height: 13px;
    fill: var(--orange);
    flex: none;
  }
  .address {
    position: absolute;
    left: 491px;
    top: 344px;
    font-style: normal;
    font-size: 18px;
    line-height: 26px;
    color: var(--ink);
    letter-spacing: 0.3px;
  }
  .footer-band {
    position: absolute;
    left: 0;
    bottom: 0;
    width: 100%;
    height: 14px;
    display: flex;
  }
  .footer-band__accent { width: 134px; background: var(--orange); }
  .footer-band__gap { width: 10px; background: var(--paper); }
  .footer-band__rule { flex: 1; background: var(--charcoal); }
</style>
</head>
<body>
<main class="canvas">
  <section class="card card--front" aria-label="Card front">
    <div class="brand brand--front">
      <span class="brand__square"></span>
      <span class="brand__name">Vornel Technologies</span>
    </div>
  </section>

  <section class="card card--back" aria-label="Card back">
    <div class="brand brand--back">
      <span class="brand__square"></span>
      <span class="brand__name">Vornel Technologies</span>
    </div>

    <div class="person">
      <h1 class="person__name">Dorian Kessler</h1>
      <p class="person__role">Managing Director</p>
    </div>

    <ul class="contact">
      <li class="contact__item">
        <svg class="contact__icon" viewBox="0 0 16 16" aria-hidden="true"><path d="M3.6 1.2l2.3 2.6-1.3 2a9 9 0 0 0 5.6 5.6l2-1.3 2.6 2.3-1.6 2.2C7.4 14.6 1.4 8.6 1.4 2.8z"/></svg>
        <span>+1 000 000 0000</span>
      </li>
      <li class="contact__item">
        <svg class="contact__icon" viewBox="0 0 16 16" aria-hidden="true"><path d="M1 3h14v1.5L8 9 1 4.5z"/><path d="M1 6.2l7 4.5 7-4.5V13H1z"/></svg>
        <span>d_kessler@vornel.tech</span>
      </li>
      <li class="contact__item">
        <svg class="contact__icon" viewBox="0 0 16 16" aria-hidden="true"><path d="M8 1a7 7 0 1 0 0 14A7 7 0 0 0 8 1zm0 1.4c.8.7 1.5 2 1.8 3.6H6.2C6.5 4.4 7.2 3.1 8 2.4zM2.5 7.2h2.6a12 12 0 0 0 0 1.6H2.5a5.6 5.6 0 0 1 0-1.6zm3.8 0h3.4a11 11 0 0 1 0 1.6H6.3a11 11 0 0 1 0-1.6zm4.6 0h2.6a5.6 5.6 0 0 1 0 1.6h-2.6a12 12 0 0 0 0-1.6zM6.2 10h3.6c-.3 1.6-1 2.9-1.8 3.6-.8-.7-1.5-2-1.8-3.6z"/></svg>
        <span>www.vornel.tech</span>
      </li>
    </ul>

    <address class="address">
      48 Harrow Lane, Suite B<br>
      London, UK B210C4
    </address>

    <div class="footer-band" aria-hidden="true">
      <span class="footer-band__accent"></span>
      <span class="footer-band__gap"></span>
      <span class="footer-band__rule"></span>
    </div>
  </section>
</main>
</body>
</html>
```